Business cards for education company

We need a business card design for a relatively new company based in Queensland and operating across Australia. We resell diploma level education courses which include Business, Management, Finance, Community Services & Government courses. We offer over 20 different courses.
The target market is for anyone 16 years of age and older. There is no age limit.

We would like to see the design use the color blue and silver. The final design should communicate professionalism and a bright future.

We sell education but are also promoting the career they see themselves in 2-3 years in the future

Our company logo is attached.

Target Market(s)

We target all age groups above 16 years of age. The main target market would be people aged between 17-35.

We focus on those people who cannot make it into University or do not want to commit the time to a full degree.

Industry/Entity Type

Education

Requirements
Must have
• Professional
Company logo
website
Contact details:

Please use the following example:

Lionel Parfitt
Senior Education Consultant
0417 386 591
Lionel.parfitt@brightwaylearninghub.com.au
www.brightwaylearninghub.com.au

```html
<!DOCTYPE html>
<html lang="en">
<head>
<meta charset="utf-8">
<title>Brightway Learning Hub – Business Card</title>
<link href="https://fonts.googleapis.com/css2?family=Open+Sans:wght@400;600;700&display=swap" rel="stylesheet">
<style>
  :root {
    --canvas-bg: #e9e9ea;
    --card-dark: #2a2725;
    --card-dark-edge: #1c1a19;
    --silver-light: #ffffff;
    --silver-mid: #e4e6e8;
    --silver-deep: #c9ccd0;
    --brand-blue: #1c8fd0;
    --accent-blue: #29b3e6;
    --accent-blue-deep: #1591c8;
    --icon-box: #3cc3ef;
    --text-white: #ffffff;
    --text-dark: #1f3f78;
  }
  * { margin: 0; padding: 0; box-sizing: border-box; }
  html, body {
    width: 1200px; height: 1023px; overflow: hidden;
    background: var(--canvas-bg);
    font-family: "Open Sans", Arial, sans-serif;
  }
  .stage {
    width: 1200px; height: 1023px;
    display: flex; align-items: center; justify-content: center;
  }
  .business-card {
    position: relative;
    width: 1050px; height: 600px;
    background: linear-gradient(160deg, #3a3633 0%, var(--card-dark) 45%, var(--card-dark-edge) 100%);
    border-radius: 6px;
    overflow: hidden;
    box-shadow: 0 18px 40px rgba(0,0,0,0.25);
  }
  .silver-band {
    position: absolute; left: 0; right: 0; top: 120px; height: 260px;
    background: linear-gradient(180deg, var(--silver-light) 0%, var(--silver-mid) 70%, var(--silver-deep) 100%);
  }
  .brand-lockup {
    position: absolute; left: 470px; top: 170px;
    display: flex; align-items: center; gap: 26px;
  }
  .brand-dot {
    width: 120px; height: 120px; border-radius: 50%;
    background: var(--brand-blue);
    flex: none;
  }
  .brand-name {
    color: var(--brand-blue);
    font-weight: 700;
    line-height: 1.05;
    text-transform: uppercase;
  }
  .brand-name .line-main { display: block; font-size: 66px; letter-spacing: 1px; }
  .brand-name .line-sub { display: block; font-size: 30px; letter-spacing: 6px; margin-top: 6px; }
  .name-bar {
    position: absolute; left: 60px; top: 318px; width: 440px; height: 92px;
    background: var(--accent-blue);
    color: var(--text-white);
    text-align: center;
    padding-top: 10px;
  }
  .person-name { font-size: 32px; font-weight: 700; letter-spacing: 0.5px; }
  .person-title { font-size: 19px; font-weight: 400; margin-top: 2px; }
  .contact-list { position: absolute; left: 0; top: 428px; list-style: none; }
  .contact-row {
    display: flex; align-items: center;
    width: 720px; height: 44px; margin-bottom: 8px;
    background: linear-gradient(90deg, var(--accent-blue) 0%, var(--accent-blue-deep) 100%);
    color: var(--text-white);
    font-size: 19px;
  }
  .contact-icon {
    width: 60px; height: 44px; flex: none;
    display: flex; align-items: center; justify-content: center;
    background: var(--icon-box);
    margin-right: 22px;
  }
  .contact-icon svg { width: 26px; height: 26px; }
  .gloss {
    position: absolute; inset: 0;
    background: linear-gradient(125deg, rgba(255,255,255,0.12) 0%, rgba(255,255,255,0) 35%);
    pointer-events: none;
  }
</style>
</head>
<body>
<main class="stage">
  <article class="business-card">
    <div class="silver-band"></div>

    <div class="brand-lockup">
      <span class="brand-dot"></span>
      <h1 class="brand-name">
        <span class="line-main">Brightway</span>
        <span class="line-sub">Learning Hub</span>
      </h1>
    </div>

    <div class="name-bar">
      <p class="person-name">Lionel Parfitt</p>
      <p class="person-title">Senior Education Consultant</p>
    </div>

    <ul class="contact-list">
      <li class="contact-row">
        <span class="contact-icon">
          <svg viewBox="0 0 24 24" fill="none" stroke="#ffffff" stroke-width="2" stroke-linejoin="round">
            <path d="M5 4h4l2 5-2.5 1.5a11 11 0 0 0 5 5L15 13l5 2v4a2 2 0 0 1-2 2A16 16 0 0 1 3 6a2 2 0 0 1 2-2z"/>
          </svg>
        </span>
        0417 386 591
      </li>
      <li class="contact-row">
        <span class="contact-icon">
          <svg viewBox="0 0 24 24" fill="none" stroke="#ffffff" stroke-width="2" stroke-linejoin="round">
            <rect x="3" y="5" width="18" height="14" rx="1"/>
            <path d="M3 6l9 7 9-7"/>
          </svg>
        </span>
        Lionel.parfitt@brightwaylearninghub.com.au
      </li>
      <li class="contact-row">
        <span class="contact-icon">
          <svg viewBox="0 0 24 24" fill="none" stroke="#ffffff" stroke-width="2">
            <circle cx="12" cy="12" r="9"/>
            <path d="M3 12h18M12 3c3 3 3 15 0 18M12 3c-3 3-3 15 0 18"/>
          </svg>
        </span>
        www.brightwaylearninghub.com.au
      </li>
    </ul>

    <div class="gloss"></div>
  </article>
</main>
</body>
</html>
```